IT Company requires new Business Card design.

Over the years we have had a few different business card designs. We are now due for new cards across the board for all staff. We felt this would be a good time to start fresh with a new design. Our traditional card simply had our details on the front, and a list of services on the back. We don't particularly need the list of services, we have had cards where the only thing on the rear of the card was our logo.
Feel free to be creative, we would like our tag line "Complete IT Management" to appear at some point, doesn't necessarily have to be with the logo.
I have attached samples and drafts of various previous cards we have used over the years.

```html
<!DOCTYPE html>
<html lang="en">
<head>
<meta charset="utf-8">
<title>Ridge Networking – Business Card</title>
<link rel="stylesheet" href="https://fonts.googleapis.com/css2?family=Arimo:wght@400;700&family=Open+Sans:wght@400;600&display=swap">
<style>
  :root {
    --backdrop: #e9e6e2;
    --card: #ffffff;
    --slate: #56636e;
    --band: #65727c;
    --ghost: #eef0f2;
    --ghost-edge: #e2e5e8;
    --ink-soft: #4a4f54;
    --on-band: #ffffff;
  }
  * { box-sizing: border-box; margin: 0; padding: 0; }
  html, body { width: 1200px; height: 992px; overflow: hidden; }
  body {
    background: var(--backdrop);
    position: relative;
    font-family: "Open Sans", sans-serif;
  }
  .card {
    position: absolute;
    top: 50px;
    width: 503px;
    height: 875px;
    background: var(--card);
    overflow: hidden;
    box-shadow: 0 2px 8px rgba(0,0,0,0.18);
  }
  .card--front { left: 79px; }
  .card--back { left: 622px; }

  .brand-mark {
    position: absolute;
    background: var(--slate);
  }
  .card--front .brand-mark { left: 55px; top: 48px; width: 78px; height: 78px; }

  .brand-name {
    position: absolute;
    font-family: "Arimo", sans-serif;
    font-weight: 700;
    color: var(--slate);
    line-height: 1;
  }
  .brand-name span { display: block; }
  .card--front .brand-name { left: 150px; top: 50px; }
  .card--front .brand-name .line-1 { font-size: 56px; letter-spacing: 1px; }
  .card--front .brand-name .line-2 { font-size: 30px; margin-top: 2px; }

  .ghost-block {
    position: absolute;
    background: var(--ghost);
    border: 2px solid var(--ghost-edge);
  }
  .card--front .ghost-block { left: 30px; top: 170px; width: 440px; height: 400px; }
  .card--back .ghost-block { left: 12px; top: 220px; width: 480px; height: 420px; }

  .address {
    position: absolute;
    left: 0; right: 0; top: 598px;
    text-align: center;
    font-size: 22px;
    color: var(--ink-soft);
  }
  .rule {
    position: absolute; left: 0; right: 0;
    height: 2px; background: var(--band);
  }
  .rule--a { top: 638px; }
  .rule--b { top: 645px; height: 1px; }

  .contact-band {
    position: absolute;
    left: 0; right: 0; top: 651px; bottom: 0;
    background: var(--band);
    color: var(--on-band);
    padding: 18px 0 0 38px;
  }
  .person { font-size: 24px; margin-bottom: 14px; }
  .person .name { font-family: "Arimo", sans-serif; font-weight: 700; }
  .person .role { font-size: 21px; }
  .contact-list { list-style: none; font-size: 20px; }
  .contact-list li { display: flex; align-items: center; height: 34px; }
  .contact-list svg { width: 20px; height: 20px; margin-right: 10px; flex: none; fill: var(--on-band); }
  .contact-list .gap { margin-left: 14px; }

  .card--back .brand-name { left: 68px; top: 355px; }
  .card--back .brand-name .line-1 { font-size: 100px; letter-spacing: 1px; }
  .card--back .brand-name .line-2 { font-size: 48px; margin-top: 4px; }
  .tagline {
    position: absolute; left: 70px; top: 500px;
    font-size: 20px; letter-spacing: 3.6px;
    color: var(--slate);
  }
  .web {
    position: absolute; left: 0; right: 0; top: 822px;
    text-align: center;
    font-size: 21px; letter-spacing: 2px;
    color: var(--slate);
  }
</style>
</head>
<body>
  <section class="card card--front">
    <div class="ghost-block" role="img" aria-label="Faint oversized brand block"></div>
    <div class="brand-mark"></div>
    <div class="brand-name"><span class="line-1">RIDGE</span><span class="line-2">NETWORKING</span></div>
    <p class="address">Unit 4 12 Marlow Street, Bayview WA 6150</p>
    <div class="rule rule--a"></div>
    <div class="rule rule--b"></div>
    <div class="contact-band">
      <p class="person"><span class="name">Daniel Reed,</span> <span class="role">Operation Manager</span></p>
      <ul class="contact-list">
        <li>
          <svg viewBox="0 0 20 20"><path d="M5 2l3 4-2 2c1 2.5 3 4.5 5.5 5.5l2-2 4 3-2 3C9 17 3 11 2 5z"/></svg>
          08 5550 1234
          <svg class="gap" viewBox="0 0 20 20"><rect x="5" y="1" width="10" height="18" rx="2"/><rect x="7" y="3" width="6" height="6" fill="#65727c"/></svg>
          0400 555 018
        </li>
        <li>
          <svg viewBox="0 0 20 20"><rect x="5" y="2" width="10" height="5"/><rect x="1" y="8" width="18" height="8" rx="1"/><rect x="5" y="13" width="10" height="5" fill="#ffffff" stroke="#65727c"/></svg>
          08 5550 1234
        </li>
        <li>
          <svg viewBox="0 0 20 20"><rect x="1" y="4" width="18" height="13" rx="1"/><path d="M1 5l9 7 9-7" fill="none" stroke="#65727c" stroke-width="1.6"/></svg>
          daniel@ridgenetworking.com.au
        </li>
        <li>
          <svg viewBox="0 0 20 20"><circle cx="10" cy="10" r="9"/><path d="M1 10h18M10 1v18M10 1c-5 5-5 13 0 18M10 1c5 5 5 13 0 18" fill="none" stroke="#65727c" stroke-width="1.3"/></svg>
          www.ridgenetworking.com.au
        </li>
      </ul>
    </div>
  </section>

  <section class="card card--back">
    <div class="ghost-block" role="img" aria-label="Faint oversized brand block"></div>
    <div class="brand-name"><span class="line-1">RIDGE</span><span class="line-2">NETWORKING</span></div>
    <p class="tagline">COMPLETE IT MANAGEMENT</p>
    <p class="web">www.ridgenetworking.com.au</p>
  </section>
</body>
</html>
```